2 Creative Website Banners for Furniture Brand

Morning Tobrasca....
The get a great night sleep banner is complete - we are happy with that one.
Ive uploaded a slightly different concept for the other banner below. This is just something rough ive thrown together. But you can see I have added a curve, a maroon coloured background which is slightly transparent and a big heart in the background....
I do not necessarily want to use this heart image but something a bit like this (a nice graphic, gif etc) but something quite elegant faded in, or perhaps a number of hearts (done in a tasteful way). Also can we keep the typography in the same format as you can see for this one.
Nearly there :)!
Industry/Entity Type
Furniture

```html
<!DOCTYPE html>
<html lang="en">
<head>
<meta charset="utf-8">
<title>Larchmere Furniture</title>
<link rel="stylesheet" href="https://fonts.googleapis.com/css2?family=Mulish:wght@300;400;600;700&family=Zilla+Slab:wght@600;700&family=Cormorant+Garamond:wght@400;500&family=Kaushan+Script&display=swap">
<style>
:root{
  --sand:#e4d9c9;
  --taupe:#a39283;
  --stone:#b3a68f;
  --plum:#5a1446;
  --pink:#f0208f;
  --ink:#1c1c1c;
  --body:#4a4a4a;
  --sale:#c0392b;
  --panel:#eeeeee;
  --mist:#e2dcdf;
  --mauve:#6b5b5e;
  --mauve-dark:#6a5a5e;
  --gold:#c9a227;
}
*{margin:0;padding:0;box-sizing:border-box}
html,body{width:717px;height:1200px;overflow:hidden;background:#fff}
body{position:relative;font-family:'Mulish',sans-serif;color:var(--ink)}
.abs{position:absolute}
.notice{left:0;top:0;width:717px;height:14px;background:var(--sand);color:#9c8656;font-size:6px;text-align:center;line-height:14px;letter-spacing:.1px}
.brand{left:29px;top:29px;width:122px;text-align:center}
.brand-name{font-size:17px;letter-spacing:5px;color:#3d2a4a;font-weight:400;line-height:18px}
.brand-sub{font-size:5px;letter-spacing:2px;color:#a08a5c;margin-top:1px;border-top:1px solid #3d2a4a;padding-top:2px}
.phone{left:563px;top:18px;font-size:14.5px;color:#3d2a4a;display:flex;align-items:center;gap:6px;letter-spacing:.5px}
.utility{left:522px;top:53px;display:flex;gap:10px;font-size:5.5px;color:#555;align-items:center}
.utility span{display:flex;align-items:center;gap:3px}
.nav{left:0;top:71px;width:717px;height:25px;background:var(--taupe)}
.nav a{position:absolute;top:0;line-height:25px;color:#fff;font-size:8.5px;text-decoration:none;transform:translateX(-50%);white-space:nowrap}
.hero{left:5px;top:96px;width:710px;height:210px;overflow:hidden}
.hero-photo{position:absolute;inset:0;background:linear-gradient(90deg,#3c3a40 0%,#4a4750 30%,#6a5a60 55%,#5b5056 75%,#4b4a52 100%)}
.hero-disc{position:absolute;left:58px;top:-49px;width:252px;height:252px;border-radius:50%;background:rgba(30,28,34,.55)}
.hero-title{position:absolute;left:87px;top:17px;font-size:21px;color:#fff;letter-spacing:.5px;white-space:nowrap}
.hero-love{position:absolute;left:73px;top:32px;font-family:'Kaushan Script',cursive;font-size:60px;color:var(--pink);letter-spacing:8px;line-height:76px;white-space:nowrap}
.hero-copy{position:absolute;left:78px;top:114px;width:214px;text-align:center;font-family:'Zilla Slab',serif;font-weight:700;font-size:12.5px;line-height:16px;letter-spacing:1.6px;color:#fff;white-space:nowrap}
.hero-cta{position:absolute;left:90px;top:173px;width:193px;height:27px;border-radius:14px;background:var(--plum);color:#fff;font-family:'Zilla Slab',serif;font-weight:700;font-size:12px;letter-spacing:2px;text-align:center;line-height:27px}
.room-tile{left:79px;top:338px;width:118px;height:118px;background:var(--stone);padding:3px}
.room-tile-frame{width:100%;height:100%;border:1px solid #fff;font-family:'Cormorant Garamond',serif;color:#fff;text-align:center;padding-top:36px}
.room-tile-small{font-size:12px;letter-spacing:5px;line-height:14px;padding-left:5px}
.room-tile-big{font-size:19px;letter-spacing:7px;color:#5e5040;margin-top:5px;line-height:20px;padding-left:7px}
.room{width:131px;text-align:center}
.room .pic{width:131px;height:131px}
.room h3{font-size:10px;font-weight:400;margin-top:9px;letter-spacing:.2px}
.room p{font-size:7.5px;color:#6b5b3e;margin-top:2px}
.section-title{font-size:13px;letter-spacing:1.8px;font-weight:300}
.section-title b{font-weight:600}
.product-pic{left:108px;top:578px;width:178px;height:225px}
.product-name{left:72px;top:834px;font-size:9.5px}
.stars{left:74px;top:847px;font-size:7px;color:var(--gold);letter-spacing:.5px}
.price{left:281px;top:834px;font-size:8px;font-weight:700;color:var(--sale)}
.price s{color:#222}
.sale{left:326px;top:852px;width:24px;height:10px;background:#b0283a;color:#fff;font-size:5px;text-align:center;line-height:10px;font-weight:700}
.pager{left:72px;top:873px;display:flex;gap:3px;align-items:center;font-size:5.5px;color:#555}
.pager i{display:block;width:10px;height:9px;background:#222}
.view-btn{left:272px;top:867px;width:78px;height:15px;background:#3b1636;color:#fff;font-size:6px;text-align:center;line-height:15px;border-radius:2px}
.usp{left:366px;width:279px;height:43px;background:var(--panel);display:flex;align-items:center}
.usp svg{margin-left:9px;flex:none}
.usp p{margin-left:11px;font-size:9.2px;line-height:9.5px;font-weight:300;width:210px}
.usp b{font-weight:600}
.about{left:366px;top:731px;width:280px;font-size:7.6px;line-height:7.9px;letter-spacing:.7px;color:var(--body);font-weight:300}
.about p{margin-bottom:7px}
.newsletter{left:0;top:969px;width:717px;height:47px;background:var(--mist)}
.newsletter h4{position:absolute;left:289px;top:17px;font-size:10px;font-weight:400;letter-spacing:.8px}
.newsletter .field{position:absolute;left:465px;top:16px;width:127px;height:18px;background:#fff;font-size:6px;color:#555;line-height:18px;padding-left:8px}
.newsletter .submit{position:absolute;left:597px;top:16px;width:48px;height:18px;background:var(--mauve-dark);color:#fff;font-size:6.5px;text-align:center;line-height:18px;letter-spacing:.6px}
.footer{left:0;top:1016px;width:717px;height:184px;background:var(--mauve);color:#fff}
.footer h5{position:absolute;top:18px;font-size:9px;font-weight:400;letter-spacing:.2px}
.footer ul{position:absolute;top:40px;list-style:none;font-size:6.3px;line-height:15.3px}
.footer .f-brand{position:absolute;left:527px;top:20px;font-size:16px;letter-spacing:5px}
.cards{position:absolute;left:72px;top:155px;display:flex;gap:3px}
.cards span{width:19.5px;height:11px;border-radius:1.5px;background:#fff}
</style>
</head>
<body>
<div class="abs notice">COVID 19 - WE ARE TAKING ORDERS AND DELIVERING AS NORMAL</div>

<div class="abs brand">
  <div class="brand-name">LARCHMERE</div>
  <div class="brand-sub">FURNITURE</div>
</div>

<div class="abs phone">
  <svg width="14" height="14" viewBox="0 0 14 14" aria-hidden="true"><circle cx="7" cy="7" r="6.5" fill="#2a3f8a"/><path d="M7 0.5v13M0.5 7h13" stroke="#fff" stroke-width="3"/><path d="M7 0.5v13M0.5 7h13" stroke="#c8102e" stroke-width="1.4"/></svg>
  0300 555 0182
</div>
<div class="abs utility">
  <span><svg width="8" height="8"><circle cx="4" cy="4" r="3.2" fill="none" stroke="#c9a227" stroke-width="1"/></svg>TRACK ORDER</span>
  <span><svg width="9" height="8" viewBox="0 0 10 9"><path d="M5 8.5 1 4.5A2.3 2.3 0 0 1 5 1.6 2.3 2.3 0 0 1 9 4.5z" fill="#c9a227"/></svg>MY WISHLIST</span>
  <span><svg width="8" height="9" viewBox="0 0 8 9"><rect x=".5" y="2.5" width="7" height="6" fill="none" stroke="#c9a227"/><path d="M2.5 2.5a1.5 1.5 0 0 1 3 0" fill="none" stroke="#c9a227"/></svg>CART <b>(0)</b></span>
</div>

<nav class="abs nav">
  <a style="left:104px">HOME</a>
  <a style="left:210px">BEDROOM &#8964;</a>
  <a style="left:336px">LIVING ROOM &#8964;</a>
  <a style="left:471px">DINING ROOM &#8964;</a>
  <a style="left:598px">CONTACT &#8964;</a>
</nav>

<section class="abs hero">
  <div class="hero-photo" role="img" aria-label="Dark grey bedroom with mirrored furniture, upholstered bed and lamp"></div>
  <div class="hero-disc"></div>
  <div class="hero-title">FIND A LOOK YOU</div>
  <div class="hero-love">LOVE</div>
  <div class="hero-copy">Lorem Ipsum not sure<br>what the rest of this will<br>say at the moment</div>
  <div class="hero-cta">SHOP BEDROOMS</div>
</section>

<div class="abs room-tile">
  <div class="room-tile-frame">
    <div class="room-tile-small">SHOP BY</div>
    <div class="room-tile-big">ROOM</div>
  </div>
</div>

<div class="abs room" style="left:220px;top:338px">
  <div class="pic" role="img" aria-label="Cream bedroom with upholstered bed and wardrobe" style="background:linear-gradient(180deg,#e9e6e2 0%,#dcd6cf 60%,#6e5040 100%)"></div>
  <h3>BEDROOM</h3><p>Collections</p>
</div>
<div class="abs room" style="left:366px;top:338px">
  <div class="pic" role="img" aria-label="Grey buttoned sofa in a light living room" style="background:linear-gradient(180deg,#ece9e6 0%,#7b8089 50%,#5d626b 75%,#c9c3bc 100%)"></div>
  <h3>LIVING ROOM</h3><p>Collections</p>
</div>
<div class="abs room" style="left:514px;top:338px">
  <div class="pic" role="img" aria-label="Light wood dining table and chairs by tall windows" style="background:linear-gradient(180deg,#eef0f1 0%,#d9d2c6 60%,#c4b8a6 100%)"></div>
  <h3>DINING ROOM</h3><p>Collections</p>
</div>

<h2 class="abs section-title" style="left:72px;top:533px">FEATURED <b>FURNITURE</b></h2>
<div class="abs product-pic" role="img" aria-label="Black four drawer chest with curved legs" style="background:linear-gradient(180deg,#2a2a2a,#141414)"></div>
<div class="abs product-name">Marguerite 4 Drawer Chest in Black</div>
<div class="abs stars">★★★★★</div>
<div class="abs price">£209.00 <s>£299.00</s></div>
<div class="abs sale">SALE</div>
<div class="abs pager"><i></i><i></i><span style="margin-left:4px">1 of 5</span></div>
<div class="abs view-btn">VIEW PRODUCT</div>

<div class="abs usp" style="top:534px">
  <svg width="26" height="24" viewBox="0 0 26 24" aria-hidden="true"><path d="M13 23 2.5 12A6 6 0 0 1 13 4.5 6 6 0 0 1 23.5 12z" fill="#2a3f8a"/><path d="M13 4.5V23M1.5 10h23" stroke="#fff" stroke-width="4"/><path d="M13 4.5V23M1.5 10h23" stroke="#c8102e" stroke-width="2"/></svg>
  <p>All of our furniture is manufactured in the <b>United Kingdom</b></p>
</div>
<div class="abs usp" style="top:585px">
  <svg width="26" height="26" viewBox="0 0 26 26" aria-hidden="true"><circle cx="13" cy="13" r="11" fill="none" stroke="#555" stroke-width="1.2" stroke-dasharray="2 1.5"/><text x="13" y="17" font-size="10" text-anchor="middle" font-family="Mulish,sans-serif" font-weight="700" fill="#333">5</text></svg>
  <p>We offer a <b>5 year guarantee</b> for complete peace of mind</p>
</div>
<div class="abs usp" style="top:636px">
  <svg width="26" height="24" viewBox="0 0 26 24" aria-hidden="true"><path d="M6 3l5 15h9" fill="none" stroke="#555" stroke-width="1.5"/><rect x="10" y="7" width="8" height="8" fill="none" stroke="#555" transform="rotate(-18 14 11)"/><circle cx="12" cy="20" r="2" fill="#555"/><circle cx="19" cy="20" r="2" fill="#555"/></svg>
  <p>All products come with <b>fast and free</b> delivery to all of mainland uk</p>
</div>

<h2 class="abs section-title" style="left:366px;top:697px"><b>HOME</b> IS WHERE THE HEART IS</h2>
<div class="abs about">
  <p>Larchmere offer a wide range of quality furniture for the bedroom, dining room or living room. Whether you want a traditional feel or ultra modern chic, we have all the latest looks and trends so you are sure to find a look you love. Finding a balance between practicality and visual appeal is also of key importance, so all of our products can be easily filtered by material, size, internal options and cost.</p>
  <p>Our bedroom ranges include bedside tables, chests of drawers, wardrobes, dressing tables, beds and innovative storage solutions - all available in a wide range of colours and materials. There are no minimum orders, so any item can be purchased individually or as part of a bedroom collection. If you’re entertaining friends or family, our living and dining room collections can transform your old look into something truly beautiful. Whether you want a real wood, high gloss, painted or laminated finish - there are many colour options and furniture styles to choose from.</p>
  <p>Many items are in stock for next day delivery or we can manufacture your order in around 14 days. Delivery is free on all furniture to mainland UK, with additional charges for some of the more remote areas. Our furniture comes flatpacked with easy home assembly required, unless the item is marked as ‘pre-assembled’.</p>
  <p>For help and advice, we offer a livechat support service or you can call us on 0300 555 0182.</p>
</div>

<section class="abs newsletter">
  <h4>SIGN UP TO OUR NEWSLETTER</h4>
  <div class="field">Enter your email address</div>
  <div class="submit">SIGN UP</div>
</section>

<footer class="abs footer">
  <h5 style="left:72px">QUICK LINKS</h5>
  <ul style="left:72px"><li>Bedroom Furniture</li><li>Living Room Furniture</li><li>Dining Room Furniture</li><li>Kid's Furniture</li></ul>
  <h5 style="left:223px">COMPANY INFO</h5>
  <ul style="left:223px"><li>About Us</li><li>Contact Us</li></ul>
  <h5 style="left:366px">DELIVERY &amp; RETURNS</h5>
  <ul style="left:366px"><li>Delivery Times</li><li>Free Delivery Areas</li><li>Returns Policy</li></ul>
  <div class="f-brand">LARCHMERE</div>
  <div class="cards"><span></span><span></span><span></span><span></span><span></span><span></span><span></span><span></span></div>
</footer>
</body>
</html>
```